TQR Habitat Stewards 2019

We need a 2 page flyer to advertise our upcoming program. The program covers 5 months May-September 2019 and is focused on conservation.I have attached some options that i like. It needs to be striking.

Text in newly uploaded document 'HSFlyer2'

Target Market(s)

Conservation
Conscious travelers
30-45 year olds
Environmental
Adventure/Hiking
Citizen Science

Font styles to use
Sans Serif

Colors
0355a3
fbed22

Requirements
Must have
• A travel conservation focus
• Highlight the significance of the 'in the world' status of the project
Nice to have
• A yellow border, making it look similar to the cover of Wanderfield Quarterly

```html
<!DOCTYPE html>
<html lang="en">
<head>
<meta charset="utf-8">
<title>TQR Habitat Stewards 2019 Flyer</title>
<link rel="stylesheet" href="https://fonts.googleapis.com/css2?family=Oswald:wght@500&family=Lato:wght@700&family=Montserrat:wght@600&display=swap">
<style>
  :root {
    --stage: #7a7a7a;
    --brand-yellow: #f0dd30;
    --brand-blue: #0355a3;
    --ink-navy: #0c1e3a;
    --white: #ffffff;
  }
  * { box-sizing: border-box; margin: 0; padding: 0; }
  html, body { width: 1200px; height: 1200px; overflow: hidden; }
  body { background: var(--stage); position: relative; }

  .flyer {
    position: absolute; left: 190px; top: 25px;
    width: 820px; height: 1150px; overflow: hidden;
  }
  .flyer__photo {
    position: absolute; inset: 0;
    background: linear-gradient(180deg,
      #4d8ee8 0%, #79b6ec 14%, #2e7fb8 22%, #3aa0c8 32%,
      #2a86b4 42%, #1b5f9e 55%, #155a98 68%, #1a5e8e 78%,
      #214f5a 88%, #2d4a2c 100%);
  }
  .frame__top {
    position: absolute; left: 22px; top: 22px; width: 787px; height: 75px;
    background: var(--brand-yellow);
  }
  .frame__side {
    position: absolute; top: 97px; width: 76px; height: 380px;
    background: linear-gradient(180deg, var(--brand-yellow) 0%, var(--brand-yellow) 70%, rgba(240,221,48,0) 100%);
  }
  .frame__side--left { left: 22px; }
  .frame__side--right { left: 733px; height: 340px; }

  .title {
    position: absolute; left: 0; width: 820px; top: 132px;
    text-align: center; color: var(--white);
    font-family: "Oswald", sans-serif; font-weight: 500;
    font-size: 92px; line-height: 1; letter-spacing: -1px;
    transform: scaleX(0.92);
    text-shadow: 3px 4px 6px rgba(0,0,0,0.35);
  }
  .title__rule {
    position: absolute; left: 120px; top: 245px; width: 582px; height: 4px;
    background: var(--white);
  }
  .intro {
    position: absolute; left: 110px; width: 610px; top: 428px;
    text-align: center; color: var(--white);
    font-family: "Lato", sans-serif; font-weight: 700;
    font-size: 24.5px; line-height: 32px; text-transform: uppercase;
    text-shadow: 0 1px 3px rgba(0,0,0,0.3);
  }
  .dates {
    position: absolute; left: 130px; top: 742px; width: 582px; height: 129px;
    border: 1px solid var(--white);
    display: flex; align-items: center; justify-content: center;
    font-family: "Oswald", sans-serif; font-weight: 500;
    font-size: 46px; color: var(--ink-navy); letter-spacing: -0.5px;
  }
  .web {
    position: absolute; left: 106px; top: 1005px; width: 516px; height: 55px;
    background: var(--brand-yellow);
    display: flex; align-items: center; justify-content: center;
    font-family: "Montserrat", sans-serif; font-weight: 600;
    font-size: 22px; letter-spacing: 4.5px; color: var(--ink-navy);
  }
  .sponsor {
    position: absolute; right: 30px; top: 1000px;
    display: flex; align-items: center; gap: 10px;
  }
  .sponsor__dot {
    width: 26px; height: 26px; border-radius: 50%; background: var(--white);
    flex: none;
  }
  .sponsor__name {
    font-family: "Lato", sans-serif; font-weight: 700;
    font-size: 17px; line-height: 20px; color: var(--white);
    text-transform: uppercase; width: 110px;
  }
</style>
</head>
<body>
  <main class="flyer">
    <div class="flyer__photo" role="img" aria-label="Aerial photo of an island lagoon with turquoise reef water, green hills on the horizon and palm forest along the lower right shore"></div>

    <div class="frame__top"></div>
    <div class="frame__side frame__side--left"></div>
    <div class="frame__side frame__side--right"></div>

    <h1 class="title">LORD HOWE ISLAND</h1>
    <div class="title__rule"></div>

    <p class="intro">The best way to experience the true beauty of Lord Howe Island is to see it for yourself; join our TQR Habitat Stewards program in 2019 and be involved in a world class, award winning holistic conservation effort – protecting paradise.</p>

    <div class="dates">5 months May-September 2019</div>

    <div class="web">www.yourwebsite.com</div>

    <div class="sponsor">
      <span class="sponsor__dot"></span>
      <span class="sponsor__name">TQR Habitat Stewards</span>
    </div>
  </main>
</body>
</html>
```